Business Card Design

Quorvel Software Limited develops and sells venue and event management software called Quorvel Stagehand, which is available in the cloud or on-premise. The company was established in 1986. Most of our customers are performing arts venues, museums and festivals. Our existing design is a bit dull. We need to convey that we are both innovative and reliable.
Not all our people show their mobile phone numbers on their cards, so the design needs to work land line and mobile or land line only.

Industry/Entity Type

Software

Contact Information for Business Card

Helen Trasko
Director
Quorvel Software Limited
42B Milbrook Lane, Epsom, Surrey, KT19 4DN
Telephone: +44 (0)1372 640913
Mobile: +44 (0)7945 216804
Email: htrasko@quorvel.net
Web: www.quorvel.net

```html
<!DOCTYPE html>
<html lang="en">
<head>
<meta charset="utf-8">
<title>Quorvel Software Limited – Business Card</title>
<link rel="stylesheet" href="https://fonts.googleapis.com/css2?family=Open+Sans:wght@400;600;700&display=swap">
<style>
  :root {
    --canvas: #e9e9ec;
    --card-dark: #242424;
    --card-light: #ffffff;
    --navy: #0d2b52;
    --blue: #0a56a3;
    --white: #ffffff;
    --shadow: rgba(0, 0, 0, 0.18);
  }
  * { box-sizing: border-box; margin: 0; padding: 0; }
  html, body {
    width: 1200px; height: 900px; overflow: hidden;
    background: var(--canvas);
    font-family: "Open Sans", Arial, sans-serif;
  }
  .stage {
    position: relative; width: 1200px; height: 900px;
    display: flex; flex-direction: column; align-items: center; justify-content: center; gap: 40px;
  }
  .card {
    position: relative; width: 660px; height: 378px;
    box-shadow: 0 10px 28px var(--shadow);
    overflow: hidden;
  }
  /* Back side */
  .card--back { background: var(--card-dark); display: flex; align-items: center; justify-content: center; }
  .brand { display: flex; align-items: center; gap: 18px; }
  .brand__square { width: 54px; height: 54px; background: var(--blue); }
  .brand__name {
    font-weight: 700; font-size: 64px; letter-spacing: 4px; line-height: 1;
    color: var(--white);
  }
  /* Front side */
  .card--front { background: var(--card-light); }
  .front__brand {
    position: absolute; left: 60px; top: 140px;
    display: flex; align-items: center; gap: 12px;
  }
  .front__brand .brand__square { width: 36px; height: 36px; }
  .front__brand .brand__name { font-size: 38px; letter-spacing: 2px; color: var(--navy); }
  .divider {
    position: absolute; left: 366px; top: 58px; width: 3px; height: 170px;
    background: linear-gradient(to bottom, rgba(13,43,82,0), var(--navy) 45%, rgba(13,43,82,0));
  }
  .contact { position: absolute; left: 392px; top: 40px; color: var(--navy); }
  .contact__name { font-weight: 700; font-size: 19px; letter-spacing: 0.5px; text-transform: uppercase; }
  .contact__role { font-weight: 600; font-size: 15px; color: var(--blue); margin: 0 0 18px 14px; }
  .contact__list { list-style: none; }
  .contact__item {
    display: flex; align-items: center; gap: 12px;
    font-weight: 600; font-size: 16px; color: var(--blue); height: 30px;
  }
  .contact__item svg { width: 18px; height: 18px; flex: none; fill: none; stroke: var(--navy); stroke-width: 1.8; }
  .contact__item svg .solid { fill: var(--navy); stroke: none; }
  .address-band {
    position: absolute; left: 0; right: 0; bottom: 30px; height: 38px;
    background: var(--navy); color: var(--white);
    display: flex; align-items: center; padding-left: 26px;
    font-weight: 600; font-size: 17px; letter-spacing: 0.3px;
  }
</style>
</head>
<body>
<main class="stage">
  <section class="card card--back" aria-label="Card back">
    <div class="brand">
      <span class="brand__square"></span>
      <span class="brand__name">QUORVEL</span>
    </div>
  </section>

  <section class="card card--front" aria-label="Card front">
    <div class="front__brand brand">
      <span class="brand__square"></span>
      <span class="brand__name">QUORVEL</span>
    </div>
    <div class="divider"></div>
    <div class="contact">
      <p class="contact__name">Helen Trasko</p>
      <p class="contact__role">Director</p>
      <ul class="contact__list">
        <li class="contact__item">
          <svg viewBox="0 0 24 24"><path class="solid" d="M6.6 10.8a15 15 0 0 0 6.6 6.6l2.2-2.2c.3-.3.7-.4 1-.2 1.1.4 2.3.6 3.6.6.6 0 1 .4 1 1V20c0 .6-.4 1-1 1A17 17 0 0 1 3 4c0-.6.4-1 1-1h3.5c.6 0 1 .4 1 1 0 1.3.2 2.5.6 3.6.1.3 0 .7-.2 1z"/></svg>
          +44 (0)1372 640913
        </li>
        <li class="contact__item">
          <svg viewBox="0 0 24 24"><rect x="7" y="2.5" width="10" height="19" rx="1.5"/><line x1="11" y1="18" x2="13" y2="18"/></svg>
          +44 (0)7945 216804
        </li>
        <li class="contact__item">
          <svg viewBox="0 0 24 24"><rect class="solid" x="2" y="5" width="20" height="14" rx="1"/><polyline points="3,6 12,13 21,6" stroke="#fff"/></svg>
          htrasko@quorvel.net
        </li>
        <li class="contact__item">
          <svg viewBox="0 0 24 24"><circle cx="12" cy="12" r="9.5"/><ellipse cx="12" cy="12" rx="4" ry="9.5"/><line x1="2.5" y1="12" x2="21.5" y2="12"/><line x1="4" y1="7" x2="20" y2="7"/><line x1="4" y1="17" x2="20" y2="17"/></svg>
          www.quorvel.net
        </li>
      </ul>
    </div>
    <div class="address-band">Quorvel Software Limited 42B Milbrook Lane, Epsom, Surrey, KT19 4DN</div>
  </section>
</main>
</body>
</html>
```